Webdesign für IT Service Firma
Zielgruppe
Wir sind eine IT-Service Firma und bieten individuelle IT-Lösungen. Unsere Kunden sind KMU, also Firmen mit einer Grösse von 2-250 Mitarbeitern im Grossraum Basel, die in Ihrem Bereich Spezialisten sind und spezielle Anforderungen an Ihre IT besitzen.
Unsere USP sind fixe Ansprechpartner, gute Erreichbarkeit, schneller und individueller Service
Aufgabenstellung
Schriftart Myriad Pro
Grün: #7FA51D
Blau: #4D9BC2
Grau: #999999
Untertitel: Wir sind da.

```html
<!DOCTYPE html>
<html lang="de">
<head>
<meta charset="utf-8">
<title>KORANI GmbH – IT Services aus Basel</title>
<link rel="stylesheet" href="https://fonts.googleapis.com/css2?family=Source+Sans+3:wght@300;400;600&family=Titillium+Web:wght@600;700&display=swap">
<style>
:root{
  --green:#7FA51D;
  --blue:#4D9BC2;
  --teal:#2A8FB0;
  --grey:#999999;
  --text:#333333;
  --muted:#555555;
  --wedge:#C9C9CA;
  --footer:#D6D6D7;
  --button:#2E8BA6;
  --backdrop:#ffffff;
}
*{margin:0;padding:0;box-sizing:border-box}
html,body{width:1200px;height:2400px;overflow:hidden;background:var(--backdrop)}
body{position:relative;font-family:"Source Sans 3",sans-serif;color:var(--text)}
h1,h2,h3{font-weight:400}
.page{position:absolute;left:236px;top:104px;width:757px;height:2165px;background:#fff;box-shadow:0 2px 8px rgba(0,0,0,.35);overflow:hidden}
.abs{position:absolute}

/* hero */
.hero{left:0;top:0;width:757px;height:359px;background:linear-gradient(120deg,#5c6166 0%,#7a7d80 40%,#8d8a82 65%,#a7a7a5 100%)}
.brand{left:18px;top:30px;font-weight:400;font-size:27px;letter-spacing:1px;color:var(--blue);display:flex;align-items:center;gap:8px}
.brand-dot{width:11px;height:11px;border-radius:50%;background:var(--green)}
.menu{left:701px;top:12px;width:37px}
.menu span{display:block;height:4px;background:var(--green);margin-bottom:6px}
.hero-title{left:28px;top:226px;font-family:"Titillium Web",sans-serif;font-weight:700;font-size:36px;line-height:50px;color:var(--green);white-space:nowrap}

/* intro */
.wedge{left:0;top:359px}
.intro-title{left:46px;top:372px;width:300px;text-align:center;font-family:"Titillium Web",sans-serif;font-weight:700;font-size:24px;line-height:32px;color:var(--teal)}
.intro-text{left:8px;top:431px;width:380px;text-align:center;font-size:19px;line-height:26.8px;color:#222;white-space:nowrap}
.services-title{left:177px;top:644px;width:500px;text-align:center;font-family:"Titillium Web",sans-serif;font-weight:700;font-size:25px;line-height:34px;color:var(--teal)}

/* service columns */
.service{top:762px;width:240px}
.service-icon{display:block;height:72px}
.service-name{width:143px;text-align:center;font-size:14px;line-height:20px;color:var(--muted);border-bottom:3px solid var(--green);padding-bottom:2px;margin-top:7px}
.service-list{list-style:none;margin-top:8px}
.service-list li{font-size:10.5px;line-height:20px;color:var(--muted);padding-left:8px;position:relative;white-space:nowrap}
.service-list li::before{content:"";position:absolute;left:0;top:8px;width:5px;height:5px;border:1px solid var(--blue);border-radius:50%}
.service-list li.cont::before{display:none}
.service-list li.cont{padding-left:0}

/* banner */
.banner{left:0;top:1199px;width:757px;height:253px;background:radial-gradient(ellipse at 45% 45%,#6f7f8c 0%,#2f3a44 35%,#1c2329 70%,#161b20 100%)}
.banner-title{left:0;top:1269px;width:757px;text-align:center;font-family:"Titillium Web",sans-serif;font-weight:700;font-size:40px;line-height:56px;color:var(--green);white-space:nowrap}

/* contact */
.contact-title{left:0;top:1467px;width:757px;text-align:center;font-size:18px;line-height:26px;color:var(--green)}
.contact-text{left:166px;top:1498px;width:436px;text-align:center;font-size:10.3px;line-height:16.8px;color:var(--muted)}
.office-title{left:128px;top:1611px;font-size:19px;line-height:26px;color:var(--green)}
.office{left:128px;top:1652px;font-size:14.5px;line-height:20px;color:var(--muted)}
.office p+p{margin-top:17px}
.field{left:396px;width:300px;height:28px;border:1px solid #aaa;font-size:10px;color:#888;padding:6px 5px}
.field.area{height:128px;width:299px;padding-top:11px}
.send{left:590px;top:1886px;width:102px;height:26px;background:var(--button);color:#fff;font-family:"Titillium Web",sans-serif;font-weight:700;font-size:11px;letter-spacing:.5px;text-align:center;line-height:26px}

/* footer */
.footer{left:0;top:1962px;width:757px;height:203px;background:var(--footer);text-align:center;color:var(--teal)}
.footer .claim{position:absolute;left:0;width:100%;top:40px;font-size:19px;line-height:26px;font-weight:300}
.footer .line{position:absolute;left:0;width:100%;font-size:15px;line-height:20px;font-weight:300}
.footer .copy{position:absolute;left:0;width:100%;top:185px;font-size:8px;line-height:10px}
</style>
</head>
<body>
<div class="page">

  <header>
    <div class="abs hero" role="img" aria-label="Foto: zwei Personen arbeiten gemeinsam an einem Bildschirm im Büro"></div>
    <div class="abs brand"><span class="brand-dot"></span>KORANI</div>
    <div class="abs menu"><span></span><span></span><span></span></div>
    <h1 class="abs hero-title">WIR KÜMMERN UNS UM IHRE IT</h1>
  </header>

  <section class="intro">
    <svg class="abs wedge" width="757" height="600" viewBox="0 0 757 600"><polygon points="0,0 514,0 0,578" fill="var(--wedge)"/></svg>
    <h2 class="abs intro-title">Wir sind da!</h2>
    <p class="abs intro-text">KORANI GmbH ist ihr Partner für IT<br>Dienstleistungen.&nbsp; Wir entwickeln Lösungen<br>aufgrund Ihrer Bedürfnisse und<br>Geschäftsprozesse. Unsere Leitgedanken<br>sind dabei der Kundenfokus, die<br>Einfachheit, sowie Robustheit<br>der Lösung.</p>
    <h2 class="abs services-title">Maßgeschneiderte Leistungen<br>für Ihr Unternehmen</h2>
  </section>

  <section class="services">
    <div class="abs service" style="left:35px">
      <svg class="service-icon" style="margin-left:23px" width="72" height="72" viewBox="0 0 80 80" fill="none" stroke="var(--teal)" stroke-width="2.5">
        <rect x="2" y="6" width="76" height="52" rx="2"/><line x1="2" y1="48" x2="78" y2="48"/>
        <path d="M32 58 L30 70 M48 58 L50 70 M18 72 H62"/>
        <path d="M40 14 L52 18 V28 C52 36 46 40 40 42 C34 40 28 36 28 28 V18 Z"/>
        <path d="M34 27 L39 32 L47 23"/>
      </svg>
      <div class="service-name">Support</div>
      <ul class="service-list">
        <li>Internetzugang installieren</li>
        <li>Problembehebung Remote bei uns vor Ort</li>
        <li>VPN / Remote-Zugriff</li>
        <li>Viren-, Trojaner- und Malware- Entfernung</li>
        <li>Drucker und Scanner</li>
        <li>Systemoptimierung</li>
        <li>Netzwerk und WLAN Konfiguration</li>
        <li>Serverinstallation</li>
        <li>Serverwartung</li>
        <li>Sichere Backup-Lösungen</li>
      </ul>
    </div>
    <div class="abs service" style="left:287px">
      <svg class="service-icon" style="margin-left:26px" width="72" height="72" viewBox="0 0 80 80" fill="none" stroke="var(--teal)" stroke-width="2.5">
        <path d="M40 4 L68 14 V38 C68 56 56 68 40 76 C24 68 12 56 12 38 V14 Z"/>
        <path d="M40 12 L60 19 V38 C60 52 52 61 40 67 C28 61 20 52 20 38 V19 Z"/>
        <rect x="29" y="36" width="22" height="17" rx="2"/>
        <path d="M33 36 V30 C33 22 47 22 47 30 V36"/>
        <circle cx="40" cy="44" r="2"/>
      </svg>
      <div class="service-name">Sicherheit</div>
      <ul class="service-list">
        <li>Verschlüsselung von Dateien, Containern</li>
        <li class="cont">und ganzen Festplatten</li>
        <li>Konfiguration von Firewalls und Switches</li>
        <li>VPN-Zugänge</li>
        <li>Verschlüsselung von vertraulicher</li>
        <li class="cont">Kommunikation, bspw. via Mail</li>
        <li class="cont">(Postora, Maillynx etc.)</li>
        <li>Verschlüsselung von Daten in der Cloud</li>
        <li>Verschlüsselung der Internetverbindung</li>
        <li class="cont">und Umleitung über Proxies.</li>
      </ul>
    </div>
    <div class="abs service" style="left:524px">
      <svg class="service-icon" style="margin-left:36px" width="72" height="72" viewBox="0 0 80 80" fill="none" stroke="var(--teal)" stroke-width="2.5">
        <path d="M14 4 H60 V44 M14 4 V74 H48"/>
        <path d="M24 16 H50 M24 26 H50 M24 36 H50 M24 46 H40 M24 56 H38"/>
        <path d="M62 44 L74 48 V58 C74 66 68 70 62 73 C56 70 50 66 50 58 V48 Z"/>
        <path d="M56 58 L61 63 L68 54"/>
      </svg>
      <div class="service-name">Beratung</div>
      <ul class="service-list">
        <li>Herstellerunabhängige Kaufberatung</li>
        <li>Infrastruktur- und Netzwerk-Planung</li>
        <li>IT-Coaching für Anwender und</li>
        <li>Entscheider</li>
        <li>IT-Supervision für Ihre internen Techniker</li>
        <li>IT-Prozessoptimierung</li>
        <li>IT-Projektleitung für Unternehmen</li>
        <li>Gestaltung von Backup Prozessen</li>
      </ul>
    </div>
  </section>

  <section>
    <div class="abs banner" role="img" aria-label="Bild: Finger berührt einen leuchtenden Fingerabdruck-Schild vor dunklem Platinen-Hintergrund"></div>
    <h2 class="abs banner-title">TECHNOLOGY FOR THE NEXT GENERATION</h2>
  </section>

  <section class="contact">
    <h2 class="abs contact-title">Wir freuen uns über Ihre Kontaktaufnahme!</h2>
    <p class="abs contact-text">Stet clita kasd gubergren, no sea takimata sanctus est Lorem ipsum dolor sit amet. Lorem ipsum dolor sit amet, consetetur sadipscing elitr, sed diam nonumy eirmod tempor invidunt ut labore et dolore magna aliquyam erat, sed diam voluptua. At vero eos et accusam et justo duo dolores et ea rebum. Stet clita kasd gubergren, no sea takimata sanctus est Lorem ipsum dolor sit amet.</p>
    <h3 class="abs office-title">Unsere Büroadresse</h3>
    <div class="abs office">
      <p>KORANI GmbH<br>Lindenhofweg 12<br>CH-4052 Basel</p>
      <p>E-Mail: support@korani.ch<br>Telefon: +41 61 000 4410<br>Fax: +41 61 000 4411</p>
    </div>
    <div class="abs field" style="top:1609px">Name</div>
    <div class="abs field" style="top:1650px">E-Mail</div>
    <div class="abs field" style="top:1694px">Telefonnummer</div>
    <div class="abs field area" style="top:1741px">Ihre Anfrage</div>
    <div class="abs send">SENDEN</div>
  </section>

  <footer class="abs footer">
    <div class="claim">IT Services aus Basel</div>
    <div class="line" style="top:80px">KORANI GmbH I Lindenhofweg 12 I CH-4052 Basel</div>
    <div class="line" style="top:106px">support@korani.ch I Tel.: +41 61 000 4410 I Fax: +41 61 000 4411</div>
    <div class="line" style="top:156px">Impressum I Datenschutz</div>
    <div class="copy">copyright Korani 2021</div>
  </footer>

</div>
</body>
</html>
```